Cafe Menu Required

We need a menu for our coffee shop.
I would like something very much the same as what I have attached.

I have attached a word doc with the items needed on the menu.

I have also attached our logo

I would like to print these on A3 size poster

Industry/Entity Type

Cafe

```html
<!DOCTYPE html>
<html lang="en">
<head>
<meta charset="utf-8">
<title>Morning Ward Canteen – Menu</title>
<link rel="stylesheet" href="https://fonts.googleapis.com/css2?family=Alfa+Slab+One&family=Zilla+Slab:wght@400&display=swap">
<style>
  :root {
    --board: #1b1b1b;
    --board-light: #262626;
    --chalk: #f4f4f2;
    --accent: #d9262c;
  }
  html, body {
    margin: 0;
    padding: 0;
    overflow: hidden;
    background: var(--board);
  }
  .menu {
    position: relative;
    width: 849px;
    height: 1200px;
    overflow: hidden;
    background: radial-gradient(ellipse at 50% 40%, var(--board-light) 0%, var(--board) 75%);
    color: var(--chalk);
    font-family: "Zilla Slab", Georgia, serif;
  }
  .brand {
    position: absolute;
    top: 118px;
    left: 0;
    width: 849px;
    display: flex;
    justify-content: center;
    align-items: center;
    gap: 14px;
  }
  .brand-dot {
    width: 22px;
    height: 22px;
    border-radius: 50%;
    background: var(--accent);
  }
  .brand-name {
    font-size: 34px;
    line-height: 44px;
    color: var(--chalk);
  }
  .tagline {
    position: absolute;
    top: 236px;
    left: 0;
    width: 849px;
    margin: 0;
    text-align: center;
    font-size: 33px;
    font-weight: 400;
    line-height: 42px;
  }
  .column {
    position: absolute;
    width: 323px;
  }
  .column-left { left: 58px; top: 336px; }
  .column-right { left: 468px; top: 336px; }
  .section-title {
    margin: 0 0 22px;
    font-family: "Alfa Slab One", Georgia, serif;
    font-weight: 400;
    font-size: 27px;
    line-height: 38px;
    color: var(--accent);
  }
  .section-title.spaced { margin-top: 68px; }
  .items {
    list-style: none;
    margin: 0;
    padding: 0;
  }
  .item {
    display: flex;
    justify-content: space-between;
    align-items: flex-start;
    margin-bottom: 16px;
    font-size: 25px;
    line-height: 31px;
  }
  .item-name { max-width: 180px; }
  .item-name.wide { max-width: 250px; }
  .item-price { white-space: nowrap; text-align: right; }
  .item-note {
    display: block;
    font-size: 21px;
    line-height: 33px;
    white-space: nowrap;
  }
</style>
</head>
<body>
<main class="menu">
  <header>
    <div class="brand">
      <span class="brand-dot"></span>
      <span class="brand-name">Morning Ward Canteen</span>
    </div>
    <h1 class="tagline">Coffee – Catering – Food To Go</h1>
  </header>

  <section class="column column-left">
    <h2 class="section-title">Hot Beverages</h2>
    <ul class="items">
      <li class="item"><span class="item-name">Espresso</span><span class="item-price">3.5</span></li>
      <li class="item"><span class="item-name">Piccolo</span><span class="item-price">3.5</span></li>
      <li class="item"><span class="item-name wide">Short Macchiato</span><span class="item-price">4.0</span></li>
      <li class="item"><span class="item-name wide">Long Macchiato</span><span class="item-price">4.5</span></li>
      <li class="item"><span class="item-name">Latte</span><span class="item-price">4/4.5/5.5</span></li>
      <li class="item"><span class="item-name">Cappucinno</span><span class="item-price">4/4.5/5.5</span></li>
      <li class="item"><span class="item-name">Flat White</span><span class="item-price">4/4.5/5.5</span></li>
      <li class="item"><span class="item-name">Long Black</span><span class="item-price">4/4.5/5.5</span></li>
      <li class="item"><span class="item-name">Hot Chocolate</span><span class="item-price">4/4.5/5.5</span></li>
      <li class="item"><span class="item-name">White Hot Chocolate</span><span class="item-price">4/4.5/5.5</span></li>
      <li class="item"><span class="item-name">Mocha</span><span class="item-price">4.5/5.0/6.0</span></li>
      <li class="item"><span class="item-name">White Choc Mocha</span><span class="item-price">4.5/5.0/6.0</span></li>
      <li class="item"><span class="item-name">Chai Latte</span><span class="item-price">4.5/5.0/6.0</span></li>
      <li class="item"><span class="item-name">Dirty Chai</span><span class="item-price">5.0/5.5/6.5</span></li>
      <li class="item"><span class="item-name wide">Selection of Teas</span><span class="item-price">3.8</span></li>
    </ul>
  </section>

  <section class="column column-right">
    <h2 class="section-title">Extras</h2>
    <ul class="items">
      <li class="item"><span class="item-name wide">Extra Shot</span><span class="item-price">0.5</span></li>
      <li class="item"><span class="item-name wide">Decaf</span><span class="item-price">0.5</span></li>
      <li class="item"><span class="item-name wide">Syrups<span class="item-note">Caramel/Hazelnut/Vanilla</span></span><span class="item-price">0.5</span></li>
      <li class="item"><span class="item-name wide">Soy</span><span class="item-price">0.5</span></li>
      <li class="item"><span class="item-name wide">Lactose free</span><span class="item-price">0.5</span></li>
    </ul>

    <h2 class="section-title spaced">Cold Beverages</h2>
    <ul class="items">
      <li class="item"><span class="item-name wide">Iced Latte</span><span class="item-price">4.5</span></li>
      <li class="item"><span class="item-name wide">Iced Long Black</span><span class="item-price">4.5</span></li>
      <li class="item"><span class="item-name">Iced Coffee w/ice cream</span><span class="item-price">6.0</span></li>
      <li class="item"><span class="item-name">Iced Chocolate w/ice cream</span><span class="item-price">6.0</span></li>
      <li class="item"><span class="item-name wide">Coffee Frappe</span><span class="item-price">6.0</span></li>
      <li class="item"><span class="item-name wide">Mango Frappe</span><span class="item-price">6.0</span></li>
    </ul>
  </section>
</main>
</body>
</html>
```